Tradeshow Booth Design

Clean background, some variance of kelly green in the colors - see image for text - maybe an image with people or nice modern homes...

Target Market(s)

Mortgage Professionals

Industry/Entity Type

Mortgage Lender

Font styles to use
Serif
Sans Serif

Colors
9bcb3c
cadf82

Requirements
Must have
• Logo, the words on the image

```html
<!DOCTYPE html>
<html lang="en">
<head>
<meta charset="utf-8">
<title>Birchwood Lending – Tradeshow Panel</title>
<link rel="stylesheet" href="https://fonts.googleapis.com/css2?family=Roboto+Condensed:wght@700&display=swap">
<style>
  :root {
    --stage: #201f20;
    --header-band: #e0e0e0;
    --sage: #93c0a8;
    --forest: #1f4a2c;
  }
  * { margin: 0; padding: 0; box-sizing: border-box; }
  html, body {
    width: 1200px;
    height: 1200px;
    overflow: hidden;
    background: var(--stage);
  }
  .panel {
    position: absolute;
    left: 43px;
    top: 200px;
    width: 1114px;
    height: 800px;
    background: var(--sage);
    font-family: "Roboto Condensed", "Arial Narrow", sans-serif;
    font-weight: 700;
    color: var(--forest);
  }
  .brand-band {
    height: 231px;
    background: var(--header-band);
    display: flex;
    align-items: center;
    justify-content: center;
    gap: 34px;
  }
  .brand-name {
    font-size: 98px;
    line-height: 1;
    letter-spacing: -1px;
  }
  .brand-dot {
    width: 110px;
    height: 110px;
    border-radius: 50%;
    background: var(--forest);
  }
  .tagline {
    position: absolute;
    top: 378px;
    font-size: 46px;
    line-height: 44px;
    text-transform: uppercase;
    letter-spacing: -0.5px;
  }
  .tagline--left { left: 120px; text-align: left; }
  .tagline--right { right: 123px; text-align: right; }
</style>
</head>
<body>
  <section class="panel">
    <header class="brand-band">
      <span class="brand-name">BIRCHWOOD</span>
      <span class="brand-dot" aria-hidden="true"></span>
      <span class="brand-name">LENDING</span>
    </header>
    <p class="tagline tagline--left">Innovative<br>Solutions for<br>Non-Traditional<br>Borrowers</p>
    <p class="tagline tagline--right">Flexible<br>Guidelines</p>
  </section>
</body>
</html>
```